Website home page re-design

I have a brochure website www.baylorwick-suites.com that allows customers to buy my product (rent meeting room or work space by the hour/day, etc or sign up for virtual office services). The mechanical aspects of the site are done and working... I just want a different, more market "correct" image on the site built around my logo, tag line and them colors (royal blue and kelly green).

Industry/Entity Type

Product

```html
<!DOCTYPE html>
<html lang="en">
<head>
<meta charset="utf-8">
<title>Baylorwick – Meeting Rooms & Virtual Office</title>
<link href="https://fonts.googleapis.com/css2?family=Lato:ital,wght@0,400;0,700;0,900;1,400;1,700&display=swap" rel="stylesheet">
<style>
:root{
  --blue:#1f2fa8;
  --blue-dark:#15207a;
  --green:#2db14a;
  --green-dark:#1f8f39;
  --ink:#333;
  --muted:#777;
  --line:#e2e2e2;
  --footer:#3a3a3a;
  --footer-dark:#2b2b2b;
  --page:#ffffff;
}
*{box-sizing:border-box;margin:0;padding:0}
html,body{width:1200px;height:2608px;overflow:hidden;background:var(--page)}
body{font-family:'Lato',sans-serif;color:var(--ink);position:relative}
.wrap{width:1040px;margin:0 auto;position:relative}
.topline{height:6px;background:var(--green)}
.header{height:122px;display:flex;align-items:center;justify-content:space-between}
.brand{display:flex;align-items:center;gap:14px;font-weight:900;font-size:44px;color:var(--blue)}
.brand-dot{width:54px;height:54px;border-radius:50%;background:var(--blue)}
.nav{display:flex;gap:4px;font-size:15px;font-weight:700}
.nav a{color:var(--blue);text-decoration:none;padding:10px 16px}
.nav a.active{background:var(--blue);color:#fff}
.hero{height:384px;background:linear-gradient(135deg,#c9d3dc,#8c98a6 55%,#56606c);position:relative}
.hero-text{position:absolute;right:80px;bottom:36px;width:600px;color:#fff;font-style:italic;font-weight:700;font-size:28px;line-height:1.25;text-align:right;text-shadow:0 2px 6px rgba(0,0,0,.35)}
.hero-bar{position:absolute;left:0;right:0;bottom:0;height:8px;background:var(--green)}
h2{font-size:30px;font-weight:700;color:var(--ink);margin-bottom:18px}
h2 .b{color:var(--blue);font-weight:900}
.about{display:flex;gap:48px;padding-top:40px;height:330px}
.about-copy{flex:1;font-size:14px;line-height:1.6;color:#555}
.tour{width:460px}
.video{height:230px;background:linear-gradient(135deg,#6d7480,#a5a9b0 60%,#3f4650);position:relative}
.video-bar{position:absolute;left:0;right:0;bottom:0;height:30px;background:#1b1b1b;display:flex;align-items:center;padding:0 10px;gap:10px}
.video-bar .track{flex:1;height:5px;background:#555}
.video-bar .track i{display:block;width:30%;height:100%;background:var(--green)}
.services{padding-top:10px;height:340px}
.svc-grid{display:grid;grid-template-columns:repeat(3,1fr);row-gap:40px;padding:6px 40px 0}
.svc{display:flex;align-items:center;gap:18px;font-weight:700;font-size:17px;color:var(--green)}
.svc svg{width:78px;height:78px;flex:none}
.btn{display:inline-block;border:2px solid var(--blue);color:var(--blue);font-weight:700;font-size:15px;padding:8px 22px;border-radius:3px}
.center{text-align:center}
.cta{background:var(--green);height:160px}
.cta .wrap{height:100%;display:flex;align-items:center;justify-content:space-between}
.cta p{color:#fff;font-style:italic;font-weight:700;font-size:30px;line-height:1.3;width:720px}
.cta .btn{border-color:#fff;color:#fff;font-size:24px;padding:14px 30px}
.video-service{padding-top:40px;height:630px}
.vs-row{display:flex;gap:30px;height:200px}
.vs-img{width:300px;height:190px;background:linear-gradient(135deg,#b9c6d4,#7a8a9a)}
.vs-copy{flex:1;font-size:14px;line-height:1.6;color:#555}
.vs-copy .btn{float:right;margin-top:10px;font-size:14px;padding:6px 16px}
.plans{display:grid;grid-template-columns:repeat(4,1fr);gap:20px;margin-top:36px;padding:0 40px}
.plan{border:1px solid var(--line);height:300px;text-align:left}
.plan-head{background:var(--blue);color:#fff;font-weight:700;font-size:18px;text-align:center;padding:12px 0;border-bottom:8px solid var(--green)}
.price{padding:18px 20px 10px;color:var(--blue);font-weight:900;font-size:42px}
.price small{font-size:16px;font-weight:400;color:var(--muted)}
.plan ul{list-style:none;padding:0 22px;font-size:14px;line-height:1.7;color:#555}
.plan li::before{content:"•";color:var(--green);margin-right:8px}
.plan .btn{display:block;margin:14px auto 0;width:110px;text-align:center;padding:5px 0;font-size:14px}
.testimonials{padding-top:40px;height:296px;background:#f6f6f6;margin-top:30px}
.t-grid{display:grid;grid-template-columns:repeat(3,1fr);gap:24px}
.t-card{background:#fff;border:1px solid var(--line);padding:18px;font-size:13px;line-height:1.6;color:#777;height:130px;font-style:italic}
.t-card b{display:block;font-style:normal;color:var(--blue);margin-top:6px}
.dots{display:flex;justify-content:center;gap:8px;margin-top:18px}
.dots i{width:10px;height:10px;border-radius:50%;background:#ccc}
.dots i.on{background:var(--blue)}
.footer{background:var(--footer);height:260px;color:#ddd;padding-top:30px;overflow:hidden}
.f-grid{display:grid;grid-template-columns:230px 280px 260px;gap:40px}
.footer h4{color:#fff;font-size:17px;margin-bottom:12px}
.footer ul{list-style:none;font-size:14px;line-height:1.8}
.footer li::before{content:"› ";color:var(--green)}
.contact p{display:flex;gap:10px;font-size:14px;line-height:1.5;margin-bottom:10px}
.contact svg{width:18px;height:18px;flex:none;margin-top:2px}
.hours{border-collapse:collapse}
.hours td{font-size:13px;line-height:1.45;padding:1px 24px 1px 0}
.bottom{background:var(--footer-dark);height:50px;color:#aaa;font-size:13px}
.bottom .wrap{height:100%;display:flex;align-items:center}
</style>
</head>
<body>
<div class="topline"></div>
<header class="wrap header">
  <div class="brand"><span class="brand-dot"></span>Baylorwick</div>
  <nav class="nav">
    <a class="active">Home</a><a>Video Conference Service</a><a>Our Services</a><a>Book An Event</a><a>Contact</a>
  </nav>
</header>

<section class="hero" role="img" aria-label="Business professionals seated around a conference table in a bright meeting room">
  <p class="hero-text">Lorem ipsum dolor sit amet, consectetuer adipiscing elit, sed diam nonummy nibh euismod tincidunt ut laoreet</p>
  <div class="hero-bar"></div>
</section>

<section class="wrap about">
  <div class="about-copy">
    <h2>About <span class="b">Baylorwick</span></h2>
    <p>Baylorwick is a full service venue designed specifically to address the meeting and work needs of legal professionals, mediators, court reporters, real estate agents, insurance agents, claims adjusters and small business owners. Rent a room by the hour or the day, host a deposition or interview, or set up a virtual office so you can focus on growing your business without the overhead of a lease.</p>
  </div>
  <div class="tour">
    <h2>Virtual Tour Vedio</h2>
    <div class="video" role="img" aria-label="Video still of a presenter in a meeting suite">
      <div class="video-bar">
        <svg width="14" height="14" viewBox="0 0 14 14"><path d="M2 1l11 6-11 6z" fill="#fff"/></svg>
        <div class="track"><i></i></div>
      </div>
    </div>
  </div>
</section>

<section class="wrap services">
  <h2>Our Services</h2>
  <div class="svc-grid">
    <div class="svc"><svg viewBox="0 0 80 80"><circle cx="40" cy="40" r="36" fill="none" stroke="var(--blue)" stroke-width="4"/><path d="M22 40l18-16 18 16v18H22z" fill="var(--blue)"/></svg>Work From Home<br>Professionals</div>
    <div class="svc"><svg viewBox="0 0 80 80"><circle cx="40" cy="40" r="36" fill="none" stroke="var(--blue)" stroke-width="4"/><path d="M20 42l20-18 20 18h-6v16H26V42z" fill="var(--blue)"/><rect x="36" y="46" width="8" height="12" fill="#fff"/></svg>Real Estate Agents</div>
    <div class="svc"><svg viewBox="0 0 80 80"><circle cx="40" cy="40" r="36" fill="none" stroke="var(--blue)" stroke-width="4"/><path d="M18 42a22 22 0 0144 0z" fill="var(--blue)"/><path d="M40 42v14a5 5 0 01-10 0" fill="none" stroke="var(--blue)" stroke-width="4"/></svg>Insurance Agents</div>
    <div class="svc"><svg viewBox="0 0 80 80"><circle cx="40" cy="40" r="36" fill="none" stroke="var(--blue)" stroke-width="4"/><rect x="30" y="22" width="22" height="12" rx="2" transform="rotate(-40 41 28)" fill="var(--blue)"/><path d="M40 34l-16 18" stroke="var(--blue)" stroke-width="6"/><rect x="22" y="54" width="24" height="5" fill="var(--blue)"/></svg>Court Reporters</div>
    <div class="svc"><svg viewBox="0 0 80 80"><circle cx="40" cy="40" r="36" fill="none" stroke="var(--blue)" stroke-width="4"/><path d="M40 20l16 6v12c0 10-7 17-16 21-9-4-16-11-16-21V26z" fill="var(--blue)"/><path d="M33 40l5 5 9-10" fill="none" stroke="#fff" stroke-width="4"/></svg>Claims Adjusters</div>
    <div class="svc"><svg viewBox="0 0 80 80"><circle cx="40" cy="40" r="36" fill="none" stroke="var(--blue)" stroke-width="4"/><path d="M40 20v36M26 26h28M30 58h20" stroke="var(--blue)" stroke-width="4"/><path d="M20 44l6-16 6 16zM48 44l6-16 6 16z" fill="var(--blue)"/></svg>Attorneys</div>
  </div>
  <p class="center" style="margin-top:30px"><span class="btn">View All</span></p>
</section>

<section class="cta">
  <div class="wrap">
    <p>Lorem ipsum dolor sit amet, consectetuer adipiscing elit, sed diam nonummy nibh euismod tincidunt ut laoreet</p>
    <span class="btn">Book An Event</span>
  </div>
</section>

<section class="wrap video-service">
  <h2>Video Conference Service</h2>
  <div class="vs-row">
    <div class="vs-img" role="img" aria-label="Team on a video conference call in a meeting room"></div>
    <div class="vs-copy">
      <p>Video conferencing is available at and hosted virtually by Baylorwick. Aligning several busy schedules in one location is hard, so whether you or your participants are located in the same city or across the country, our video service lets you schedule conferences, interviews, depositions and mediations without travel. Save time, money and frustration with a connection that simply works from any location.</p>
      <span class="btn">Read More</span>
    </div>
  </div>
  <div class="plans">
    <div class="plan"><div class="plan-head">Hourly</div><div class="price">$95 <small>/hour</small></div><ul><li>includes first 2 sites</li><li>$40 per additional site</li><li>$75 setup fee</li></ul><span class="btn">Sign Up</span></div>
    <div class="plan"><div class="plan-head">Bronze</div><div class="price">$750 <small>/hour</small></div><ul><li>includes 1-10 sites</li><li>unlimited time</li><li>$50 setup fee per event</li></ul><span class="btn">Sign Up</span></div>
    <div class="plan"><div class="plan-head">Silver</div><div class="price">$1,300 <small>/hour</small></div><ul><li>includes 11-20 sites</li><li>unlimited time</li><li>$50 setup fee per event</li></ul><span class="btn">Sign Up</span></div>
    <div class="plan"><div class="plan-head">Gold</div><div class="price">$1,900 <small>/hour</small></div><ul><li>includes 21-30 sites</li><li>unlimited time</li><li>$50 setup fee per event</li></ul><span class="btn">Sign Up</span></div>
  </div>
</section>

<section class="testimonials">
  <div class="wrap">
    <h2>Client Testimonials</h2>
    <div class="t-grid">
      <div class="t-card">Lorem ipsum dolor sit amet, consectetuer adipiscing elit, sed diam nonummy nibh euismod tincidunt ut laoreet dolore magna aliquam.<b>Lorem ipsum dolor sit</b></div>
      <div class="t-card">Lorem ipsum dolor sit amet, consectetuer adipiscing elit, sed diam nonummy nibh euismod tincidunt ut laoreet dolore magna aliquam.<b>Lorem ipsum dolor sit</b></div>
      <div class="t-card">Lorem ipsum dolor sit amet, consectetuer adipiscing elit, sed diam nonummy nibh euismod tincidunt ut laoreet dolore magna aliquam.<b>Lorem ipsum dolor sit</b></div>
    </div>
    <div class="dots"><i class="on"></i><i></i><i></i></div>
  </div>
</section>

<footer class="footer">
  <div class="wrap f-grid">
    <div><h4>Quick Links</h4><ul><li>Home</li><li>Video Conference Service</li><li>Our Services</li><li>Book An Event</li><li>Contact</li></ul></div>
    <div class="contact"><h4>Contact Details</h4>
      <p><svg viewBox="0 0 18 18"><path d="M9 1a6 6 0 016 6c0 5-6 10-6 10S3 12 3 7a6 6 0 016-6z" fill="var(--green)"/><circle cx="9" cy="7" r="2" fill="var(--footer)"/></svg>1480 Alder Row<br>Ferncastle TN 37900</p>
      <p><svg viewBox="0 0 18 18"><path d="M4 1l3 4-2 2a10 10 0 006 6l2-2 4 3-2 3C8 17 1 10 1 3z" fill="var(--green)"/></svg>800-555-0172</p>
      <p><svg viewBox="0 0 18 18"><rect x="1" y="4" width="16" height="11" fill="var(--green)"/><path d="M1 4l8 6 8-6" fill="none" stroke="var(--footer)" stroke-width="1.5"/></svg>info@baylorwick-suites.com</p>
    </div>
    <div><h4>Business Hours</h4>
      <table class="hours"><tr><td>Mon</td><td>8 am to 6 pm</td></tr><tr><td>Tue</td><td>8 am to 6 pm</td></tr><tr><td>Wed</td><td>8 am to 6 pm</td></tr><tr><td>Thu</td><td>8 am to 6 pm</td></tr><tr><td>Fri</td><td>8 am to 6 pm</td></tr><tr><td>Sat</td><td>Closed</td></tr><tr><td>Sun</td><td>Closed</td></tr></table>
    </div>
  </div>
</footer>
<div class="bottom"><div class="wrap">© Baylorwick 2015 &nbsp;|&nbsp; All Rights Reserved</div></div>
</body>
</html>
```